serious, thorough, light and simple - that's my advice and mediations

My business card should combine my logo (uploaded file) and my homepage (https://fellor-mediation.webnestsite.com).

Contact Information for Business Card

Name: Sabine Fellor di Vanti
Phone: 076 412 58 94
mail: sfellor@postkiv.ch
web: www.fellor-di-vanti.ch

```html
<!DOCTYPE html>
<html lang="de">
<head>
<meta charset="utf-8">
<title>Sabine Fellor di Vanti – Business Card</title>
<link href="https://fonts.googleapis.com/css2?family=Work+Sans:wght@400;600&display=swap" rel="stylesheet">
<style>
  :root {
    --bg: #d0d1cc;
    --paper: #ffffff;
    --blue: #2b3a86;
    --blue-mid: #4a4d7a;
    --mauve: #6e6069;
    --gold: #a98552;
    --ink: #4a4a4a;
  }
  html, body {
    margin: 0;
    width: 1200px;
    height: 1058px;
    overflow: hidden;
    background: var(--bg);
    font-family: "Work Sans", sans-serif;
  }
  .card {
    position: absolute;
    left: 250px;
    width: 700px;
    height: 400px;
    box-shadow: 0 14px 30px rgba(0,0,0,0.18);
    overflow: hidden;
  }
  .card--front { top: 90px; background: var(--paper); }
  .card--back {
    top: 568px;
    background: linear-gradient(100deg, var(--blue) 0%, var(--blue-mid) 30%, var(--mauve) 60%, var(--gold) 100%);
  }
  .card__waves { position: absolute; inset: 0; }

  .brand {
    position: absolute;
    display: flex;
    align-items: center;
    gap: 12px;
  }
  .brand__dot {
    width: 34px; height: 34px;
    border-radius: 50%;
    border: 3px solid currentColor;
    box-sizing: border-box;
  }
  .brand__name {
    font-weight: 600;
    white-space: nowrap;
  }
  .card--front .brand { left: 40px; top: 156px; color: var(--gold); }
  .card--front .brand__name { font-size: 21px; }
  .card--back .brand {
    left: 0; right: 0; top: 170px;
    justify-content: center;
    color: #ffffff;
  }
  .card--back .brand__dot { width: 52px; height: 52px; }
  .card--back .brand__name { font-size: 40px; }

  .divider {
    position: absolute;
    left: 336px; top: 108px;
    width: 2px; height: 130px;
    background: var(--blue);
  }
  .contact {
    position: absolute;
    left: 362px; top: 76px;
    color: var(--ink);
  }
  .contact__name {
    margin: 0;
    font-size: 23px;
    font-weight: 600;
    color: var(--blue);
  }
  .contact__role {
    margin: 4px 0 18px;
    font-size: 16px;
  }
  .contact__list { list-style: none; margin: 0; padding: 0; }
  .contact__item {
    display: flex;
    align-items: center;
    gap: 10px;
    font-size: 17px;
    line-height: 28px;
  }
  .contact__icon { width: 13px; height: 13px; fill: none; stroke: var(--blue); stroke-width: 1.6; }
</style>
</head>
<body>

<section class="card card--front" aria-label="Business card front">
  <svg class="card__waves" viewBox="0 0 700 400" preserveAspectRatio="none" aria-hidden="true">
    <defs>
      <linearGradient id="waveBlue" x1="0" y1="0" x2="1" y2="0">
        <stop offset="0" stop-color="#2b3a86"/>
        <stop offset="0.6" stop-color="#4a4d7a"/>
        <stop offset="1" stop-color="#6e6069"/>
      </linearGradient>
    </defs>
    <path d="M0 400 L0 326 C220 350 480 340 700 286 L700 400 Z" fill="#a98552"/>
    <path d="M0 334 C220 358 480 350 700 298" fill="none" stroke="#ffffff" stroke-width="4"/>
    <path d="M0 400 L0 340 C220 366 480 362 700 312 L700 400 Z" fill="url(#waveBlue)"/>
  </svg>

  <div class="brand">
    <span class="brand__dot" aria-hidden="true"></span>
    <span class="brand__name">Klarweg Mediation</span>
  </div>

  <div class="divider" aria-hidden="true"></div>

  <div class="contact">
    <h1 class="contact__name">Sabine Fellor di Vanti</h1>
    <p class="contact__role">Director</p>
    <ul class="contact__list">
      <li class="contact__item">
        <svg class="contact__icon" viewBox="0 0 16 16"><path d="M4 1.5 L6.5 4.5 L5 6.5 C6 8.5 7.5 10 9.5 11 L11.5 9.5 L14.5 12 L13 14.5 C7 14 2 9 1.5 3 Z"/></svg>
        076 412 58 94
      </li>
      <li class="contact__item">
        <svg class="contact__icon" viewBox="0 0 16 16"><rect x="1.5" y="3.5" width="13" height="9"/><path d="M1.5 3.5 L8 9 L14.5 3.5"/></svg>
        sfellor@postkiv.ch
      </li>
      <li class="contact__item">
        <svg class="contact__icon" viewBox="0 0 16 16"><circle cx="8" cy="8" r="6.5"/><path d="M1.5 8 H14.5 M8 1.5 C5 5 5 11 8 14.5 C11 11 11 5 8 1.5"/></svg>
        www.fellor-di-vanti.ch
      </li>
    </ul>
  </div>
</section>

<section class="card card--back" aria-label="Business card back">
  <div class="brand">
    <span class="brand__dot" aria-hidden="true"></span>
    <span class="brand__name">Klarweg Mediation</span>
  </div>
</section>

</body>
</html>
```